Business Card Design Project

Brightfern Consulting is a newly created boutique consultancy focussing on delivering strategic consulting to medium and large businesses, with a focus on:
- Strategic planning and execution.
- Corporate function optimisation, especially in the areas of finance, commercial, and IT. This includes implementing the right functional design for the needs of the business, and ensuring the right skills.
- Performance management, in particular project governance and control, operational metrics and management reporting.
I have in mind a tag line for the business being:
"Guiding companies toward lasting growth."
I am looking for a letterhead design which utilises my new logo on report templates (powerpoint and word), and letterhead.
Trivopedix defines a mother lode as follows:
"Mother lode is a principal vein or zone of veins of gold or silver ore. The term probably came from a literal translation of the Spanish veta madre, a term common in old Mexican mining. Veta madre, for instance, is the name given to an 11-kilometre-long (6.8 mi) silver vein discovered in 1548 in Guanajuato, New Spain (modern-day Mexico)."
My preference is for black and gold. Logo files are attached in .eps format. All fonts are outlined. The fonts that are used are "Crimson Text" and "Josefin Sans". They are free open source fonts and they are available here: http://www.typevault.example/fonts
Target Market(s)
Medium to large corporates.
Industry/Entity Type
Boutique
Font styles to use
Other font styles liked:
- All Fonts Are Outlined. The Fonts That Are Used Are "Crimson Text" And "Josefin Sans". They Are Free Open Source Fonts And They Are Available Here: Http://www.typevault.example/fonts
Look and feel
Each slider illustrates characteristics of the customer's brand and the style your logo design should communicate.

```html
<!DOCTYPE html>
<html lang="en">
<head>
<meta charset="utf-8">
<title>Brightfern Consulting — Business Cards</title>
<link rel="stylesheet" href="https://fonts.googleapis.com/css2?family=Crimson+Text:ital,wght@0,400;0,600;1,400&display=swap">
<style>
  :root {
    --backdrop: #e4e4e4;
    --card: #141414;
    --card-edge: #1d1d1d;
    --gold: #d9a521;
    --white: #f4f4f4;
    --grey: #b5b5b5;
  }
  * { margin: 0; padding: 0; box-sizing: border-box; }
  html, body { width: 1200px; height: 750px; overflow: hidden; }
  body {
    background: radial-gradient(ellipse at 45% 35%, #f1f1f1 0%, var(--backdrop) 60%, #d3d3d3 100%);
    position: relative;
    font-family: "Crimson Text", Georgia, serif;
  }
  .card {
    position: absolute;
    top: 230px;
    width: 500px;
    height: 290px;
    border-radius: 26px;
    background: linear-gradient(160deg, var(--card-edge), var(--card));
    box-shadow: 0 14px 30px rgba(0,0,0,0.25);
  }
  .card--contact { left: 70px; }
  .card--brand { left: 630px; }

  /* contact card */
  .holder { position: absolute; top: 38px; right: 60px; text-align: right; }
  .holder__name { color: var(--gold); font-size: 26px; font-weight: 600; letter-spacing: 0.5px; line-height: 1.1; }
  .holder__role { color: var(--grey); font-size: 15px; line-height: 1.2; padding-right: 14px; }
  .contact-mark {
    position: absolute; left: 58px; top: 112px;
    width: 74px; height: 74px;
    border: 6px solid var(--white);
  }
  .contact-list {
    position: absolute; left: 58px; top: 196px;
    list-style: none;
    display: grid; grid-template-columns: auto auto; column-gap: 6px;
  }
  .contact-list li { display: contents; }
  .contact-list .label { color: var(--grey); font-style: italic; font-size: 16px; line-height: 22px; text-align: right; }
  .contact-list .value { color: var(--gold); font-weight: 600; font-size: 16px; line-height: 22px; white-space: nowrap; }

  /* brand card */
  .brand { position: absolute; left: 0; right: 0; top: 48px; text-align: center; }
  .brand__square {
    display: block; margin: 0 auto 18px;
    width: 84px; height: 84px;
    border: 7px solid var(--white);
  }
  .brand__name {
    color: var(--white); font-size: 30px; font-weight: 400;
    letter-spacing: 1px; text-transform: uppercase; line-height: 1.1;
  }
  .brand__rule { width: 230px; height: 2px; background: var(--gold); margin: 6px auto 0; }
  .brand__tagline {
    position: absolute; left: 0; right: 0; bottom: 42px;
    text-align: center; color: var(--gold); font-size: 16px; font-weight: 600;
  }
</style>
</head>
<body>
  <section class="card card--contact" aria-label="Contact side">
    <div class="holder">
      <p class="holder__name">Daniel Reyes</p>
      <p class="holder__role">C.E.O.</p>
    </div>
    <span class="contact-mark" aria-hidden="true"></span>
    <ul class="contact-list">
      <li><span class="label">phone:</span><span class="value">+0198 765 432</span></li>
      <li><span class="label">email:</span><span class="value">hello@brightfern.net</span></li>
      <li><span class="label">web:</span><span class="value">www.brightfern.com.au</span></li>
    </ul>
  </section>

  <section class="card card--brand" aria-label="Brand side">
    <div class="brand">
      <span class="brand__square" aria-hidden="true"></span>
      <p class="brand__name">Brightfern Consulting</p>
      <div class="brand__rule"></div>
    </div>
    <p class="brand__tagline">Guiding companies toward lasting growth.</p>
  </section>
</body>
</html>
```